Medical Practice Brochure Design Project

We are a medical practice in Denver, Colorado and we need to design a brochure to promote one subset of services we offer. We perform Bureau of Roadway Oversight (BRO) physical exams and also perform BRO drug testing onsite and want a brochure that outlines these services. This brochure will be used a part of a marketing package to promote this service to businesses that employ individuals that drive commercial vehicles.

Project Deadline Extended Reason: I am going extend the deadline for submissions. Ending on a Sunday is going to limit last minute submissions. As a trade off, I am going to guarantee this project. Thanks for all the submissions. Added Thursday, October 09, 2014

Target Market(s)

human resource managers, companies that deploy commercial vehicles (i.e. trucks and tractor trailers), independent drivers / contractors

Industry/Entity Type

Medical

Font styles to use
Sans Serif

Colors
0455a3

Requirements
Must have
• Our logo, our web address (larkfieldclinichub.com), our phone number and fax number, professional look and feel, layout be a trifold 8.5x11 (see templates), map to our location (see attached for example).
Nice to have
• Our logo (bellweather family medicine) should not be the focus of the brochure. Text items that should stand out should be "BRO Examination", "BRO Drug Testing" and "QVLPA Certified Providers", our phone number, and our web address. We also will have the ability to have clients schedule appointment online through our website which should be indicated in the brochure in a prominent manner.
Should not have
• no images of crosses, no images of syringes

```html
<!DOCTYPE html>
<html lang="en">
<head>
<meta charset="utf-8">
<title>BRO Exam Trifold Brochure – Outside Panels</title>
<link rel="stylesheet" href="https://fonts.googleapis.com/css2?family=Open+Sans:wght@400;600;700&display=swap">
<style>
  :root {
    --page-bg: #ececec;
    --paper: #ffffff;
    --paper-shade: #f1f2f4;
    --brand-blue: #0455a3;
    --heading-blue: #0a4f96;
    --accent-orange: #f6a623;
    --body-text: #4a4f57;
    --fold-line: #d9dce1;
    --photo-light: #c9d2e6;
    --photo-mid: #8f9fcb;
    --photo-dark: #5a6aa6;
  }
  * { box-sizing: border-box; margin: 0; padding: 0; }
  html, body {
    width: 1200px;
    height: 635px;
    overflow: hidden;
    background: var(--page-bg);
    font-family: "Open Sans", Arial, sans-serif;
  }
  .canvas {
    width: 1200px;
    height: 635px;
    display: flex;
    align-items: center;
    justify-content: center;
  }
  .brochure {
    position: relative;
    width: 780px;
    height: 603px;
    background: var(--paper);
    box-shadow: 0 6px 24px rgba(0,0,0,0.12);
    display: flex;
  }
  .cover-art {
    position: absolute;
    top: 0;
    left: 0;
    width: 780px;
    height: 330px;
    z-index: 1;
  }
  .panel {
    position: relative;
    width: 260px;
    height: 100%;
    z-index: 2;
  }
  .panel + .panel { border-left: 1px solid var(--fold-line); }
  .panel--middle { background: linear-gradient(to bottom, var(--paper) 70%, var(--paper-shade)); }
  .panel__body {
    position: absolute;
    left: 24px;
    right: 22px;
  }
  .panel--exam .panel__body { top: 326px; }
  .panel--quote .panel__body { top: 262px; }
  .panel--testing .panel__body { top: 238px; }
  .panel__title {
    color: var(--heading-blue);
    font-weight: 700;
    line-height: 1.08;
    margin-bottom: 10px;
  }
  .panel--exam .panel__title { font-size: 23px; letter-spacing: 0.3px; }
  .panel--quote .panel__title,
  .panel--testing .panel__title { font-size: 19px; }
  .panel__text {
    font-size: 9.6px;
    line-height: 1.48;
    color: var(--body-text);
    text-align: justify;
  }
  .web-address {
    color: var(--brand-blue);
    font-weight: 600;
    font-size: 10.5px;
    letter-spacing: 0.2px;
  }
  .panel--exam .web-address,
  .panel--quote .web-address {
    position: absolute;
    left: 24px;
    bottom: 26px;
  }
  .panel--testing .web-address {
    display: block;
    margin-top: 10px;
  }
</style>
</head>
<body>
<main class="canvas">
  <section class="brochure" aria-label="BRO exam brochure, outside panels">
    <svg class="cover-art" viewBox="0 0 780 330" aria-hidden="false">
      <defs>
        <linearGradient id="photoTone" x1="0" y1="0" x2="1" y2="1">
          <stop offset="0" stop-color="var(--photo-light)"/>
          <stop offset="0.45" stop-color="var(--photo-mid)"/>
          <stop offset="1" stop-color="var(--photo-dark)"/>
        </linearGradient>
      </defs>
      <path class="swoosh swoosh--orange" fill="var(--accent-orange)"
            d="M0 0 H260 V248 C190 326 72 330 0 304 Z"/>
      <path class="swoosh swoosh--blue" fill="var(--brand-blue)"
            d="M520 0 H780 V168 C700 214 600 228 520 226 Z"/>
      <g role="img" aria-label="Photograph of a white ambulance parked outdoors, spread across the three panels">
        <path fill="url(#photoTone)" d="M0 0 H260 V226 C190 302 72 306 0 282 Z"/>
        <path fill="url(#photoTone)" d="M260 0 H520 V214 C450 250 330 258 260 236 Z"/>
        <path fill="url(#photoTone)" d="M520 0 H780 V150 C700 196 600 210 520 210 Z"/>
      </g>
    </svg>

    <article class="panel panel--exam">
      <div class="panel__body">
        <h2 class="panel__title">BRO EXAM</h2>
        <p class="panel__text">For commercial motor vehicle drivers, the most important safety feature is YOU – the driver! Each time you turn the key, you are responsible for your own safety, as well as the safety of all the people who share the road with you. The physical examination you take for your medical certificate confirms that you are healthy enough to safely perform the demanding job of a commercial motor vehicle driver and keep our Nation's roads safe.1</p>
      </div>
      <span class="web-address">www.larkfieldclinichub.com</span>
    </article>

    <article class="panel panel--quote panel--middle">
      <div class="panel__body">
        <h2 class="panel__title">1=quote from the NRSOA website</h2>
        <p class="panel__text">Commercial motor vehicle drivers must maintain a current Medical Examiners Certificate to drive. Drivers must have their exam completed by a QVLPA certified provider. BRO examinations determine a driver's physical qualification to operate a commercial motor vehicle. Medical Examiners Certificates must be renewed at least every two years.</p>
      </div>
      <span class="web-address">www.larkfieldclinichub.com</span>
    </article>

    <article class="panel panel--testing">
      <div class="panel__body">
        <h2 class="panel__title">Bureau of Roadway Oversight Drug Testing</h2>
        <p class="panel__text">We offer BRO and Non-BRO drug testing onsite and this can be done on the same day as your BRO exam.</p>
        <span class="web-address">www.larkfieldclinichub.com</span>
      </div>
    </article>
  </section>
</main>
</body>
</html>
```